Tarnabee Wines - web page for new Australian wine label

We need a landing page for our wine company. Tarnabee is a family owned company, we grow the gapes, and make the wine in the Clare valley. Daniel Hovsted is the winemaker and is well known for his style, which is all about the fruit flavour rather than wood or age influences. Tarnabee is Abriginal for 2 hills and a water source. We hand pick, hand plunge, foot crush resulting in elegant wine. Little to no additives, minimal filtering, single vineyard wines. Handcrafted with small releases of only the best fruit from carefully selected rows and bunches. The Clare valley is located two hours North of Adelaide, is known for cool climate and slow ripening, resulting in wines that have an elegant mouth feel, with bright colour and outstanding flavours. Our Sevenhill vineyard has a Eastern aspect, gathering morning sun and escaping the hot afternoons, and in our opinion is on of the prettiest valleys in the world. Only 1000 cases per annum of the very best handpicked fruit, from the best rows. We hope you enjoy the Tarnabee style, the reds are lighter in colour, fruit driven palate, more old world influence and the Riesling is on the dry side with fresh citrus. Minimal additives and filtering, our aim was to make wine with minimal influence from wine making. Handcrafted wines.

Target Market(s)

females 18 - 60 are the ones that buy 70 percent of wine, so whilst men are also a target, its the ladies we seek to appeal to.

Industry/Entity Type

It Company

Number of Pages Required

4 page

Font styles to use
Serif

Requirements
Must have
• Eye catching front page that makes me feel like i am ordering from quality company, that cares for what they do. Easy to use ordering, and delivery instructions.
• postage is $14.90 per case Australia wide.
• www.tarnabeewines.com
Nice to have
• I want to see a fun and family oriented business that cares for the wine, we dont make a lot, its buckets and feet. But its wine made wanting to be the best in the world, we dont cut corners on quality. Handcrafted
Should not have
• dont really have any thoughts here, looking for all ideas

```html
<!DOCTYPE html>
<html lang="en">
<head>
<meta charset="utf-8">
<title>Tarnabee Wines – Family Owned Wine Company</title>
<link rel="stylesheet" href="https://fonts.googleapis.com/css2?family=Lato:wght@300;400;700&family=Lora:ital,wght@0,400;0,700;1,400&family=Pacifico&display=swap">
<style>
  :root {
    --blue: #0d6fc0;
    --overlay-blue: rgba(74, 150, 210, 0.78);
    --ink: #1c1c1c;
    --text: #2e2e2e;
    --muted: #777777;
    --grey-band: #e6e6e6;
    --card-border: #d9d9d9;
    --footer: #3a3a3a;
    --footer-line: #4d4d4d;
    --white: #ffffff;
    --star: #f5b800;
    --heading-navy: #17325c;
  }
  * { box-sizing: border-box; margin: 0; padding: 0; }
  html, body { width: 1200px; height: 2452px; overflow: hidden; }
  body { position: relative; background: var(--white); font-family: "Lato", sans-serif; color: var(--text); }
  .abs { position: absolute; }
  .serif { font-family: "Lora", serif; }

  /* Header */
  .site-header { position: absolute; left: 0; top: 0; width: 1200px; height: 123px; background: var(--white); }
  .brand { position: absolute; left: 87px; top: 40px; display: flex; align-items: center; gap: 12px;
           font-family: "Lora", serif; font-weight: 400; font-size: 42px; color: var(--blue); }
  .brand-dot { width: 14px; height: 14px; border-radius: 50%; background: var(--blue); }
  .main-nav { position: absolute; right: 87px; top: 58px; display: flex; gap: 18px; }
  .main-nav a { font-size: 14.5px; color: var(--ink); text-decoration: none; text-transform: uppercase; position: relative; }
  .main-nav a.is-active::after { content: ""; position: absolute; left: -2px; right: -2px; top: 30px; height: 3px; background: var(--blue); }

  /* Hero */
  .hero { position: absolute; left: 0; top: 123px; width: 1200px; height: 549px;
          background: linear-gradient(160deg, #8a7f7a 0%, #a79a92 30%, #6d4f52 60%, #a9545a 85%, #7d4648 100%); }
  .hero-arrow { position: absolute; top: 262px; }
  .hero-panel { position: absolute; left: 216px; top: 276px; width: 791px; height: 193px; background: var(--overlay-blue); text-align: center; }
  .hero-title { margin-top: 36px; font-family: "Pacifico", cursive; font-size: 50px; color: var(--white); font-weight: 400; line-height: 1.2; }
  .hero-sub { font-family: "Lato", sans-serif; font-weight: 300; font-size: 36px; color: var(--white); letter-spacing: 1px; text-transform: uppercase; margin-top: 2px; }
  .btn-white { position: absolute; background: var(--white); color: var(--ink); text-transform: uppercase; font-family: "Lato", sans-serif;
               display: flex; align-items: center; justify-content: center; text-decoration: none; }
  .hero-buy { left: 942px; top: 340px; width: 162px; height: 63px; font-size: 19px; border-radius: 2px; }

  /* About */
  .section-script { font-family: "Pacifico", cursive; font-weight: 400; color: var(--ink); }
  .about-title { left: 87px; top: 740px; font-size: 25px; }
  .about-title::after { content: ""; display: block; width: 114px; height: 3px; background: var(--blue); }
  .about-copy { left: 87px; top: 816px; width: 545px; font-size: 12.4px; line-height: 18px; color: var(--ink); text-align: justify; }
  .about-copy p + p { margin-top: 18px; }
  .btn-blue { position: absolute; background: var(--blue); color: var(--white); border-radius: 3px; font-size: 13px;
              display: flex; align-items: center; justify-content: center; text-decoration: none; }
  .read-more { left: 87px; top: 1012px; width: 117px; height: 41px; }
  .photo-harvest-crew { left: 708px; top: 770px; width: 291px; height: 224px; background: linear-gradient(180deg, #9fbfdc 0%, #c5cfd6 35%, #6a7a4e 60%, #5a5240 100%); }
  .photo-grape-picker { left: 870px; top: 934px; width: 243px; height: 188px; border: 3px solid var(--white);
                        background: linear-gradient(160deg, #8a7a5a 0%, #a55a3a 45%, #d06a2a 70%, #6f4e3a 100%); }

  /* Featured wine */
  .wine-band { position: absolute; left: 0; top: 1174px; width: 1200px; height: 507px; }
  .wine-visual { position: absolute; left: 0; top: 0; width: 574px; height: 507px; background: var(--grey-band); }
  .bottle-area { position: absolute; left: 212px; top: 44px; width: 102px; height: 401px; border-radius: 30px 30px 8px 8px;
                 background: linear-gradient(90deg, #1a1214 0%, #3a2a2e 45%, #140e10 100%); }
  .wine-info { position: absolute; left: 574px; top: 0; width: 626px; height: 507px; background: var(--blue); color: var(--white); }
  .wine-name { position: absolute; left: 70px; top: 63px; font-family: "Lora", serif; font-size: 21px; font-weight: 700; line-height: 27px; text-transform: uppercase; }
  .wine-copy { position: absolute; left: 70px; top: 132px; width: 440px; font-size: 12px; line-height: 22px; }
  .wine-copy p + p { margin-top: 22px; }
  .wine-buy { left: 70px; top: 391px; width: 180px; height: 50px; font-size: 21px; border-radius: 2px; }

  /* Testimonials */
  .testimonials-title { left: 0; width: 1200px; top: 1750px; text-align: center; font-size: 22px; color: var(--heading-navy); }
  .testimonials-rule { left: 543px; top: 1793px; width: 114px; height: 3px; background: var(--blue); }
  .quote-card { position: absolute; top: 1830px; width: 500px; height: 157px; border: 2px solid var(--card-border); background: var(--white); }
  .quote-card p { margin: 38px 26px 0; font-style: italic; font-size: 12.8px; line-height: 22px; color: var(--muted); }
  .quote-tail { position: absolute; left: 234px; bottom: -20px; }
  .reviewer { position: absolute; top: 2008px; display: flex; align-items: flex-start; gap: 18px; }
  .avatar { width: 102px; height: 102px; border-radius: 50%; border: 2px solid #6a8db0; background: linear-gradient(180deg, #d9d2cb 0%, #b08f7d 100%); }
  .reviewer-info { padding-top: 32px; }
  .reviewer-name { font-size: 18px; font-weight: 700; color: var(--ink); }
  .reviewer-name span { font-size: 13.5px; font-weight: 400; }
  .stars { display: flex; margin-top: 8px; margin-left: 60px; }

  /* Footer */
  .site-footer { position: absolute; left: 0; top: 2194px; width: 1200px; height: 258px; background: var(--footer); color: var(--white); }
  .footer-brand { position: absolute; left: 87px; top: 58px; font-family: "Lora", serif; font-size: 40px; line-height: 50px; color: var(--blue); display: flex; align-items: center; gap: 12px; }
  .subscribe { position: absolute; left: 87px; top: 131px; display: flex; }
  .subscribe-input { width: 206px; height: 43px; background: var(--white); color: #555; font-size: 13px; display: flex; align-items: center; padding-left: 14px; }
  .subscribe-btn { width: 44px; height: 43px; background: var(--blue); display: flex; align-items: center; justify-content: center; }
  .footer-heading { position: absolute; top: 50px; font-size: 22px; font-weight: 400; }
  .contact-list { position: absolute; left: 513px; top: 90px; list-style: none; font-size: 13px; }
  .contact-list li { display: flex; align-items: center; gap: 6px; height: 20px; margin-bottom: 12px; }
  .quick-links { position: absolute; top: 89px; list-style: none; font-size: 13px; line-height: 22px; }
  .footer-bottom { position: absolute; left: 0; top: 209px; width: 1200px; height: 1px; background: var(--footer-line); }
  .copyright { position: absolute; left: 87px; top: 227px; font-size: 13px; }
  .social { position: absolute; left: 548px; top: 228px; display: flex; gap: 16px; }
  .social span { width: 14px; height: 14px; border-radius: 50%; background: var(--white); display: block; }
</style>
</head>
<body>

<header class="site-header">
  <div class="brand"><span class="brand-dot"></span>Tarnabee</div>
  <nav class="main-nav">
    <a href="#" class="is-active">Home</a>
    <a href="#">Wine</a>
    <a href="#">About Us</a>
    <a href="#">Wine Room</a>
    <a href="#">Heritage</a>
    <a href="#">Contact</a>
    <a href="#">Blog</a>
  </nav>
</header>

<section class="hero" role="img" aria-label="Children smiling beside grape crushing tubs at the winery">
  <svg class="hero-arrow" style="left:30px" width="16" height="30" viewBox="0 0 16 30"><path d="M14 2 L2 15 L14 28" fill="none" stroke="#fff" stroke-width="2"/></svg>
  <svg class="hero-arrow" style="left:1142px" width="16" height="30" viewBox="0 0 16 30"><path d="M2 2 L14 15 L2 28" fill="none" stroke="#fff" stroke-width="2"/></svg>
  <div class="hero-panel">
    <h1 class="hero-title">Welcome to Tarnabee</h1>
    <p class="hero-sub">Family Owned Wine Company</p>
  </div>
  <a href="#" class="btn-white hero-buy">Buy Now</a>
</section>

<section class="about">
  <h2 class="abs section-script about-title">About Tarnabee</h2>
  <div class="abs about-copy serif">
    <p>Tarnabee is a family owned wine company in the Clare Valley, two hours north of Adelaide. We grow the grapes and make the wine ourselves: hand picked, hand plunged and foot crushed, with buckets, feet and a lot of care. Winemaker Daniel Hovsted is known for a style built on fruit flavour rather than wood or age.</p>
    <p>Our Sevenhill vineyard faces east, catching the morning sun and escaping the hot afternoons. Slow ripening gives wines of bright colour and an elegant mouth feel. Little to no additives, minimal filtering, and only 1000 cases a year from the best rows. Tarnabee means two hills and a water source.</p>
  </div>
  <a href="#" class="btn-blue read-more">Read More &gt;</a>
  <div class="abs photo-harvest-crew" role="img" aria-label="Harvest crew standing among the vineyard rows"></div>
  <div class="abs photo-grape-picker" role="img" aria-label="Picker holding up a bunch of dark grapes in the vineyard"></div>
</section>

<section class="wine-band">
  <div class="wine-visual">
    <div class="bottle-area" role="img" aria-label="Bottle of 2016 Reserve Shiraz"></div>
  </div>
  <div class="wine-info">
    <h2 class="wine-name">2016 Reserve Shiraz<br>Tarnabee Vineyard</h2>
    <div class="wine-copy serif">
      <p>Single vineyard Shiraz from our Sevenhill rows, hand picked and foot crushed in small batches. Lighter in colour with a bright, fruit driven palate and a gentle old world edge. Made with minimal additives and filtering, so the fruit does the talking in every glass.</p>
      <p>Ordering is easy: add a case to your cart, pay securely at checkout and we ship within two business days. Postage is a flat $14.90 per case Australia wide, signature on delivery.</p>
    </div>
    <a href="#" class="btn-white wine-buy">Buy Now</a>
  </div>
</section>

<section class="testimonials">
  <h2 class="abs section-script testimonials-title">Customer Testimonials</h2>
  <div class="abs testimonials-rule"></div>

  <div class="quote-card" style="left:87px">
    <p class="serif">"The Shiraz is bright, juicy and beautifully light on the palate. You can taste the care in every glass, and my case arrived in two days."</p>
    <svg class="quote-tail" width="36" height="20" viewBox="0 0 36 20"><path d="M0 0 L18 18 L36 0" fill="#fff" stroke="#d9d9d9" stroke-width="2"/></svg>
  </div>
  <div class="quote-card" style="left:613px">
    <p class="serif">"A dry, fresh Riesling with real citrus zing. Ordering took a minute, postage was simple, and the whole family now asks for Tarnabee."</p>
    <svg class="quote-tail" width="36" height="20" viewBox="0 0 36 20"><path d="M0 0 L18 18 L36 0" fill="#fff" stroke="#d9d9d9" stroke-width="2"/></svg>
  </div>

  <div class="reviewer" style="left:160px">
    <div class="avatar" role="img" aria-label="Portrait of Marla J Whitcombe"></div>
    <div class="reviewer-info">
      <div class="reviewer-name">Marla J Whitcombe, <span>New Jersey.</span></div>
      <div class="stars">
        <svg width="86" height="16" viewBox="0 0 86 16"><g fill="#f5b800"><path id="st" d="M8 0 L10 5.5 L16 6 L11.5 9.8 L13 16 L8 12.6 L3 16 L4.5 9.8 L0 6 L6 5.5Z"/><use href="#st" x="17.5"/><use href="#st" x="35"/><use href="#st" x="52.5"/><use href="#st" x="70"/></g></svg>
      </div>
    </div>
  </div>
  <div class="reviewer" style="left:684px">
    <div class="avatar" role="img" aria-label="Portrait of Brennan"></div>
    <div class="reviewer-info">
      <div class="reviewer-name">Brennan, <span>New Jersey.</span></div>
      <div class="stars" style="margin-left:28px">
        <svg width="86" height="16" viewBox="0 0 86 16"><g fill="#f5b800"><use href="#st"/><use href="#st" x="17.5"/><use href="#st" x="35"/><use href="#st" x="52.5"/><use href="#st" x="70"/></g></svg>
      </div>
    </div>
  </div>
</section>

<footer class="site-footer">
  <div class="footer-brand"><span class="brand-dot"></span>Tarnabee</div>
  <div class="subscribe">
    <div class="subscribe-input">Subscribe Your Email</div>
    <div class="subscribe-btn">
      <svg width="20" height="18" viewBox="0 0 20 18"><path d="M0 8 L20 0 L16 18 L9 12 L17 3 L7 11 Z" fill="#fff"/></svg>
    </div>
  </div>

  <h3 class="footer-heading" style="left:513px">To Reach Us:</h3>
  <ul class="contact-list">
    <li><svg width="10" height="14" viewBox="0 0 10 14"><path d="M5 0 C2 0 0 2.2 0 5 C0 8.5 5 14 5 14 C5 14 10 8.5 10 5 C10 2.2 8 0 5 0Z M5 7 A2 2 0 1 1 5 3 A2 2 0 1 1 5 7Z" fill="#fff"/></svg> - 58 Orchard Lane, Sevenhill, SA 5453.</li>
    <li><svg width="12" height="12" viewBox="0 0 12 12"><path d="M2.5 0 L4.5 3 L3.2 4.5 C4 6.2 5.8 8 7.5 8.8 L9 7.5 L12 9.5 L10.5 12 C5 11.5 0.5 7 0 1.5Z" fill="#fff"/></svg> - (08) 555 0142</li>
    <li><svg width="13" height="10" viewBox="0 0 13 10"><rect width="13" height="10" fill="#fff"/><path d="M0 0 L6.5 5.5 L13 0" fill="none" stroke="#3a3a3a" stroke-width="1.2"/></svg> - info@tarnabeewines.com</li>
  </ul>

  <h3 class="footer-heading" style="left:912px">Quick Links:</h3>
  <ul class="quick-links" style="left:912px">
    <li>&gt; Home</li><li>&gt; Wine</li><li>&gt; About Us</li>
  </ul>
  <ul class="quick-links" style="left:1037px">
    <li>&gt; Wine Room</li><li>&gt; Heritage</li><li>&gt; Contact</li>
  </ul>

  <div class="footer-bottom"></div>
  <p class="copyright">Tarnabee © Copyrights 2017. All rights reserved.</p>
  <div class="social" aria-label="Social links"><span></span><span></span><span></span><span></span></div>
</footer>

</body>
</html>
```